TITLE: What Makes My Child’s Playing Talent Grow? SUB-TITLE: A Mother’s Plain Talk Manual for Coaching...

My book is for parents who have young children that are really into sports. My book empowers parents so they can motivate their children to succeed. It deals with sports psychology. Both my title and subtitle should be easy to read. Ideally, I would like a picture of young athlete(s) on the title. I have uploaded files of some books on Brindlemart that deal with the same subject. The last two files are 1) my company logo, please try to include these colors 2) an ebook cover I put together myself. You will notice an On-line bonus in the middle of the book, this Bonus needs to be on the cover.

Target Market(s)

Parents with children who play sports at a high level

Colors

Designer to choose colors to be used in the design.

Requirements
Must have
• Online Bonus feature as per my example.
• Dimensions: Pagelux = The ideal size of your eBook cover art is a height/width ratio of 1.6:1. This means that for every 1,000 pixels in width, the image should be 1,600 pixels in height.
Nice to have
• picture of a young athlete or young athletes

```html
<!DOCTYPE html>
<html lang="en">
<head>
<meta charset="utf-8">
<title>What Makes My Child’s Playing Talent Grow? — Book Cover</title>
<link href="https://fonts.googleapis.com/css2?family=Russo+One&family=Crimson+Text:wght@600&display=swap" rel="stylesheet">
<style>
  :root {
    --page-bg: #ffffff;
    --cover-black: #0d0d0d;
    --ink-white: #ffffff;
    --ink-black: #111111;
    --badge-gold: #d08a2a;
    --badge-rim: #a8631a;
    --badge-ink: #3a1f05;
    --logo-orange: #e9962e;
  }
  * { box-sizing: border-box; margin: 0; padding: 0; }
  html, body {
    width: 1200px; height: 1106px; overflow: hidden;
    background: var(--page-bg);
  }
  .cover {
    position: absolute; left: 270px; top: 33px;
    width: 660px; height: 1040px;
    background: var(--cover-black);
    font-family: "Russo One", sans-serif;
    color: var(--ink-white);
    overflow: hidden;
  }
  .tagline {
    position: absolute; top: 38px; left: 0; width: 100%;
    text-align: center; font-size: 21px; line-height: 1.35;
    letter-spacing: 0.3px; text-transform: uppercase;
  }
  .athlete-strip {
    position: absolute; top: 125px; left: 0; width: 100%; height: 240px;
    display: flex;
  }
  .athlete-strip .panel { flex: 1; height: 100%; }
  .panel.rings   { background: linear-gradient(180deg, #2e5d78, #1b3446); }
  .panel.runner  { background: linear-gradient(180deg, #0f1a22, #1d4a3a); }
  .panel.hockey  { background: linear-gradient(180deg, #27496b, #dfe8ef); }
  .panel.soccer  { background: linear-gradient(180deg, #2a3e5e, #2f6a2a); }
  .panel.gymnast { background: linear-gradient(180deg, #f1f1f3, #c9c6d8); }
  .panel.karate  { background: linear-gradient(180deg, #3a6aa8, #1c3a66); }
  .panel.skater  { background: linear-gradient(180deg, #4d6f90, #c6d3e0); }
  .title {
    position: absolute; top: 395px; left: 0; width: 100%;
    text-align: center; text-transform: uppercase; white-space: nowrap;
    line-height: 1;
  }
  .title .lead  { font-size: 50px; margin-bottom: 18px; }
  .title .big   { font-size: 88px; margin-bottom: 8px; }
  .title .mid   { font-size: 60px; margin-bottom: 10px; }
  .title .final { font-size: 96px; }
  .bonus-badge {
    position: absolute; left: 270px; top: 785px;
    width: 120px; height: 120px; border-radius: 50%;
    background: radial-gradient(circle at 40% 35%, #e6a445, var(--badge-gold) 60%, var(--badge-rim));
    border: 4px dotted var(--badge-rim);
    display: flex; flex-direction: column; align-items: center; justify-content: center;
    font-family: "Crimson Text", serif; color: var(--badge-ink);
    text-align: center; line-height: 1.05;
  }
  .bonus-badge .offer { font-size: 14px; text-transform: uppercase; }
  .bonus-badge .value { font-size: 17px; margin-top: 3px; }
  .bonus-badge .note  { font-size: 8px; margin-top: 2px; }
  .author-band {
    position: absolute; left: 0; bottom: 0; width: 100%; height: 125px;
    background: var(--ink-white);
    display: flex; align-items: center; justify-content: center; gap: 22px;
  }
  .author-name { color: var(--ink-black); font-size: 58px; text-transform: uppercase; letter-spacing: 1px; }
  .brand-dot { width: 40px; height: 40px; border-radius: 50%; background: var(--logo-orange); }
</style>
</head>
<body>
  <main class="cover">
    <p class="tagline">A Mother’s Plain Talk Manual for Coaching<br>Confident, Focused and Resilient Athletes</p>

    <div class="athlete-strip">
      <div class="panel rings" role="img" aria-label="Young gymnast on the rings"></div>
      <div class="panel runner" role="img" aria-label="Young sprinter in motion"></div>
      <div class="panel hockey" role="img" aria-label="Young ice hockey player"></div>
      <div class="panel soccer" role="img" aria-label="Young soccer player kicking a ball"></div>
      <div class="panel gymnast" role="img" aria-label="Young rhythmic gymnast with ribbon"></div>
      <div class="panel karate" role="img" aria-label="Young karate athlete mid kick"></div>
      <div class="panel skater" role="img" aria-label="Young figure skater"></div>
    </div>

    <h1 class="title">
      <div class="lead">What Makes</div>
      <div class="big">My Child’s</div>
      <div class="mid">Playing Talent</div>
      <div class="final">Grow?</div>
    </h1>

    <div class="bonus-badge">
      <span class="offer">Free<br>Online<br>Workshop</span>
      <span class="value">$170 Value</span>
      <span class="note">Details Inside</span>
    </div>

    <div class="author-band">
      <span class="author-name">Teo Marquand</span>
      <span class="brand-dot"></span>
    </div>
  </main>
</body>
</html>
```